Dark Comedy Movie Poster

We need a poster design for our short film BRAM that we just wrapped on.
It's a dark comedy
Bram explores the world of loneliness through the lens of a manic man-child. Bram wants nothing more than the approval of others, giving every last bit of energy to the cause. But his ravenous attempts accomplish the opposite, turning others off. His desperation is authentic, his lonliness cavernous.
Here is a link to the film
https://clipvault.example/548207316
Password: Bram42
I want you, the artist, to pitch me an idea in any way you want. I'm open to absolutely anything right now. Once I have some pitches from you all my production team and I will sort through them and pick the best fit!
-Owen

```html
<!DOCTYPE html>
<html lang="en">
<head>
<meta charset="utf-8">
<title>BRAM – Poster</title>
<link href="https://fonts.googleapis.com/css2?family=Amatic+SC:wght@400;700&family=Oswald:wght@400;500&display=swap" rel="stylesheet">
<style>
  :root {
    --stage: #2a2a2c;
    --teal: #3f9fb0;
    --teal-deep: #2f8797;
    --teal-light: #7cc3cf;
    --paper: #f4f6f4;
    --wash-blue: #d3e9ef;
    --wash-yellow: #f3ecbf;
    --title-red: #8e2b2b;
    --ink: #3a2222;
    --photo-dark: #2a1f1c;
    --photo-mid: #8a5a44;
    --photo-light: #c99a7e;
  }
  * { margin: 0; padding: 0; box-sizing: border-box; }
  html, body {
    width: 1200px; height: 960px; overflow: hidden;
    background: var(--stage);
  }
  .poster {
    position: absolute; left: 362px; top: 40px;
    width: 476px; height: 880px;
    background: var(--teal);
    overflow: hidden;
  }
  .poster__backdrop {
    position: absolute; inset: 0;
    background: radial-gradient(ellipse at 30% 30%, var(--teal-light) 0%, var(--teal) 45%, var(--teal-deep) 100%);
    opacity: .85;
  }
  .poster__message {
    position: absolute; inset: 0;
    font-family: "Amatic SC", cursive;
    color: rgba(230, 245, 248, .55);
    text-transform: uppercase;
    letter-spacing: 3px;
  }
  .poster__message span { position: absolute; white-space: nowrap; line-height: 1; }
  .msg-congrats { left: 10px; top: 24px; font-size: 38px; }
  .msg-accomplished { right: 10px; top: 74px; font-size: 38px; }
  .msg-youve { left: 10px; top: 84px; font-size: 38px; }
  .msg-goals { right: 10px; top: 180px; font-size: 42px; }
  .msg-all-you { left: 10px; top: 222px; font-size: 44px; }
  .msg-ever { right: 10px; top: 240px; font-size: 100px; }
  .msg-all-on { left: 10px; top: 340px; font-size: 54px; }
  .msg-one { right: 10px; top: 420px; font-size: 100px; }
  .msg-sin { left: 10px; top: 440px; font-size: 72px; }
  .poster__lower {
    position: absolute; left: 0; top: 0; width: 476px; height: 880px;
  }
  .poster__photo {
    position: absolute; left: 88px; top: 86px;
    width: 272px; height: 470px;
    border-radius: 6px;
    background: linear-gradient(180deg, var(--photo-dark) 0%, var(--photo-mid) 35%, var(--photo-light) 70%, var(--paper) 100%);
  }
  .poster__title {
    position: absolute; left: 148px; width: 140px; top: 612px;
    text-align: center;
    font-family: "Amatic SC", cursive; font-weight: 400;
    font-size: 84px; line-height: 1; color: var(--title-red);
    letter-spacing: 1px;
  }
  .credits {
    position: absolute; left: 0; top: 718px; width: 476px; height: 100px;
    font-family: "Oswald", sans-serif; color: var(--ink);
    text-transform: uppercase; text-align: center;
  }
  .credit { position: absolute; width: 110px; margin-left: -55px; }
  .credit__role { display: block; font-size: 6px; letter-spacing: 1px; opacity: .8; line-height: 1.4; }
  .credit__name { display: block; font-size: 11px; font-weight: 500; letter-spacing: .4px; line-height: 1.2; }
  .credit--minor .credit__name { font-size: 7px; font-weight: 400; }
  .c-lead-a { left: 130px; top: 0; }
  .c-director { left: 233px; top: 4px; }
  .c-lead-b { left: 330px; top: 12px; }
  .c-dop { left: 147px; top: 52px; }
  .c-editor { left: 233px; top: 58px; }
  .c-producer { left: 333px; top: 66px; }
</style>
</head>
<body>
  <main class="poster">
    <div class="poster__backdrop"></div>
    <div class="poster__message">
      <span class="msg-congrats">Congrats Bram</span>
      <span class="msg-accomplished">accomplished</span>
      <span class="msg-youve">You've</span>
      <span class="msg-goals">goals</span>
      <span class="msg-all-you">All you</span>
      <span class="msg-ever">Er</span>
      <span class="msg-all-on">All on</span>
      <span class="msg-one">One</span>
      <span class="msg-sin">Sin</span>
    </div>

    <svg class="poster__lower" viewBox="0 0 476 880" aria-hidden="true">
      <path d="M0 620 C40 560 90 520 150 500 C200 485 260 480 300 500 C360 520 420 540 476 560 L476 880 L0 880 Z" fill="var(--paper)"/>
      <path d="M0 560 C30 530 70 530 110 560 C120 620 110 690 80 760 L0 790 Z" fill="var(--wash-blue)" opacity=".8"/>
      <path d="M250 520 C320 500 400 520 476 540 L476 700 C420 720 330 720 270 690 C255 640 250 580 250 520 Z" fill="var(--wash-yellow)"/>
    </svg>

    <div class="poster__photo" role="img" aria-label="Photograph of the lead actor, head and shoulders, facing the viewer"></div>

    <h1 class="poster__title">BRAM</h1>

    <section class="credits">
      <p class="credit c-lead-a"><span class="credit__role">Starring</span><span class="credit__name">Miles Hartley</span></p>
      <p class="credit c-director"><span class="credit__role">Written &amp; Directed</span><span class="credit__name">Owen Tarrow</span></p>
      <p class="credit c-lead-b"><span class="credit__role">Starring</span><span class="credit__name">Jonah Pell</span></p>
      <p class="credit credit--minor c-dop"><span class="credit__role">DOP</span><span class="credit__name">Noah Reyes</span></p>
      <p class="credit credit--minor c-editor"><span class="credit__role">Editor</span><span class="credit__name">Tess Lawn</span></p>
      <p class="credit credit--minor c-producer"><span class="credit__role">Produced by</span><span class="credit__name">Dara Finch</span></p>
    </section>
  </main>
</body>
</html>
```